A-Frame Advertisement Board

I would like to have these images in an A-frame advertisement board. I need people to see this board and know straight away what it is that we do.<br/>I would like to advertise our Summer Training Program and Winter Training program.<br/><br/>Each picture needs to have an advertisement for Summer and Winter.<br/><br/>I would like to have written on each photo:<br/>Summer Training Program <br/>and <br/>Winter Training Program<br/><br/>I really liked how you designed our car graphic and the way the colours and writing looked.<br/><br/>Height: 1225mm<br/>Width: 945mm<br/><br/>

```html
<!DOCTYPE html>
<html lang="en">
<head>
<meta charset="utf-8">
<title>Training Program A-Frame Boards</title>
<link rel="stylesheet" href="https://fonts.googleapis.com/css2?family=Teko:wght@600&family=Russo+One&family=Ubuntu:wght@700&display=swap">
<style>
  :root {
    --canvas-bg: #ececec;
    --ink-black: #131313;
    --frame-white: #ffffff;
    --program-red: #e0231c;
    --summer-yellow: #fff23a;
    --summer-orange: #f57f1c;
    --winter-blue-light: #7fd0f5;
    --winter-blue: #2a8fd6;
    --silver-light: #ffffff;
    --silver-mid: #a9a9a9;
    --sky-top: #9fd8ec;
    --sky-summer: #f0e7c4;
    --sky-winter: #e4f1f6;
    --grass-light: #a9c64a;
    --grass-deep: #4f8a2b;
    --kit-navy: #1f3a73;
  }
  * { box-sizing: border-box; margin: 0; padding: 0; }
  html, body { width: 1200px; height: 656px; overflow: hidden; }
  body {
    background: var(--canvas-bg);
    position: relative;
  }
  .board {
    position: absolute;
    top: 28px;
    width: 463px;
    height: 600px;
    overflow: hidden;
    background: var(--ink-black);
  }
  .board--summer { left: 107px; }
  .board--winter { left: 630px; }

  .board__photo {
    position: absolute;
    inset: 0;
  }
  .board--summer .board__photo {
    background: linear-gradient(180deg, var(--sky-top) 0%, var(--sky-summer) 52%, var(--grass-light) 68%, var(--grass-deep) 100%);
  }
  .board--winter .board__photo {
    background: linear-gradient(180deg, var(--sky-top) 0%, var(--sky-winter) 50%, var(--grass-light) 70%, var(--grass-deep) 100%);
  }
  .board__players {
    position: absolute;
    border-radius: 40% 40% 8% 8%;
  }
  .board--summer .board__players {
    left: 60px; top: 268px; width: 340px; height: 290px;
    background: radial-gradient(ellipse at 50% 45%, rgba(31,58,115,0.75), rgba(31,58,115,0.15) 70%, transparent 72%);
  }
  .board--winter .board__players {
    left: 150px; top: 262px; width: 230px; height: 300px;
    background: radial-gradient(ellipse at 50% 45%, rgba(31,58,115,0.75), rgba(31,58,115,0.15) 70%, transparent 72%);
  }

  .board__brush {
    position: absolute;
    left: 0; top: 0;
    width: 463px; height: 600px;
  }

  .title-box {
    position: absolute;
    left: 98px;
    top: 34px;
    width: 286px;
    height: 300px;
    border: 3px solid var(--frame-white);
    transform: rotate(-2deg);
    text-align: center;
    padding: 0 10px;
  }
  .board--winter .title-box { transform: rotate(1.5deg); }

  .title-box__season,
  .title-box__training {
    font-family: "Teko", "Arial Narrow", sans-serif;
    font-weight: 600;
    line-height: 0.82;
    display: inline-block;
    padding: 0 8px;
    -webkit-background-clip: text;
    background-clip: text;
    color: transparent;
    transform: skewX(-6deg);
  }
  .title-box__season {
    font-size: 86px;
    margin-top: 30px;
  }
  .board--summer .title-box__season {
    background-image: linear-gradient(180deg, var(--summer-yellow) 20%, var(--summer-orange) 95%);
  }
  .board--winter .title-box__season {
    background-image: linear-gradient(180deg, var(--winter-blue-light) 15%, var(--winter-blue) 90%);
  }
  .title-box__training {
    font-size: 76px;
    margin-top: 4px;
    background-image: linear-gradient(180deg, var(--silver-light) 30%, var(--silver-mid) 55%, var(--silver-light) 80%);
  }
  .title-box__program {
    display: block;
    font-family: "Russo One", sans-serif;
    font-size: 38px;
    line-height: 1;
    color: var(--program-red);
    margin-top: 8px;
    letter-spacing: -0.5px;
  }

  .board__url {
    position: absolute;
    bottom: 26px;
    font-family: "Ubuntu", sans-serif;
    font-weight: 700;
    font-size: 24px;
    color: var(--frame-white);
    -webkit-text-stroke: 1px var(--ink-black);
    paint-order: stroke fill;
    text-shadow: 0 2px 3px rgba(0,0,0,0.6);
    white-space: nowrap;
  }
  .board--summer .board__url { left: 92px; transform: rotate(2deg); }
  .board--winter .board__url { right: 92px; transform: rotate(-2deg); }
</style>
</head>
<body>

  <section class="board board--summer">
    <div class="board__photo" role="img" aria-label="Sunny rugby training field with palm leaves in the corners"></div>
    <div class="board__players" role="img" aria-label="Three young rugby players in team kit running a tackle-bag drill"></div>
    <svg class="board__brush" viewBox="0 0 463 600" aria-hidden="true">
      <polygon points="0,58 463,40 463,330 380,350 300,352 60,360 0,378" fill="var(--ink-black)"/>
      <polygon points="40,120 70,118 70,124 40,126" fill="var(--sky-top)"/>
      <polygon points="400,300 463,296 463,304 400,308" fill="var(--sky-top)"/>
    </svg>
    <div class="title-box">
      <span class="title-box__season">SUMMER</span>
      <span class="title-box__training">TRAINING</span>
      <span class="title-box__program">PROGRAM</span>
    </div>
    <p class="board__url">www.torvik.com.au</p>
  </section>

  <section class="board board--winter">
    <div class="board__photo" role="img" aria-label="Cool rugby training field framed with pale snowflake shapes"></div>
    <div class="board__players" role="img" aria-label="Young rugby player in blue kit running with the ball beside a tackle bag"></div>
    <svg class="board__brush" viewBox="0 0 463 600" aria-hidden="true">
      <polygon points="0,38 463,52 463,322 400,340 300,348 80,344 0,330" fill="var(--ink-black)"/>
      <polygon points="20,100 60,98 60,104 20,106" fill="var(--sky-top)"/>
      <polygon points="410,110 463,108 463,116 410,118" fill="var(--sky-top)"/>
    </svg>
    <div class="title-box">
      <span class="title-box__season">WINTER</span>
      <span class="title-box__training">TRAINING</span>
      <span class="title-box__program">PROGRAM</span>
    </div>
    <p class="board__url">www.torvik.com.au</p>
  </section>

</body>
</html>
```